Willowmere Acres Brand - Bag Design

We are a company dealing with nuts, grains and seeds and are looking for a design for our retail bag packaging that will be consistent across all our product range. We are currently differentiating in way of color but please feel free to be more creative if you wish. Sample of products include pumpkin seeds, rolled oats, almonds, etc.
Design Idea: Hygienic, Natural (from Nature), Quality & Upscale, Simple & Clean design
Target Market: High-end Markets, end-users of A/B type.
1. Bag size is 210 mm (width) * 310 mm (length). Material is OPP or multi-layer PP.
2. Front must have clear window to show packed products. Back clear window is optional.
3. Front side must have logo that stands out (Willowmere Acres) as attached.
4. Front side must have product name and net weight.
5. Back side must have enough space for Nutrition Fact, product descriptions (110 mm * 100 mm), and barcode.
6. Back side must have white space to print production and expiry dates about 25 mm * 30 mm.
7. Top and bottom of bag must be opaque and not show product.
Updates
Project Deadline Extended
Reason: Extended period for more new ideas and also for requested modification.
Target Market(s)
Premium market. Type A to B customers as well as professional clients. The product is not a snack. It is for cooking or baking.
Industry/Entity Type
Food Store
Requirements
Must have
- Look unique and stand out from others in the market.
- The colors of the word "Willowmere Acres" and the blue air-brush in the logo can be changed.
Nice to have
- See project description
Should not have
- See project description

```html
<!DOCTYPE html>
<html lang="en">
<head>
<meta charset="utf-8">
<title>Willowmere Acres — Bag Range</title>
<link rel="stylesheet" href="https://fonts.googleapis.com/css2?family=Oswald:wght@700&family=Montserrat:wght@600;700&display=swap">
<style>
  :root {
    --stage: #efe6da;
    --white: #f7f7f5;
    --pumpkin-top: #e38a10;
    --pumpkin-body: #c4700f;
    --pumpkin-deep: #a85c0c;
    --nuts-top: #8e8177;
    --nuts-body: #a89d8b;
    --nuts-deep: #938774;
    --logo-ink: #3b5aa3;
    --badge: rgba(255,255,255,0.85);
  }
  * { margin: 0; padding: 0; box-sizing: border-box; }
  html, body { width: 1200px; height: 1200px; overflow: hidden; }
  body { background: var(--stage); position: relative; }
  .bag { position: absolute; top: 300px; width: 410px; height: 600px; }
  .bag--pumpkin { left: 110px; }
  .bag--nuts { left: 680px; }
  .bag svg { width: 100%; height: 100%; display: block; }
  .brand-name { font-family: "Montserrat", sans-serif; font-weight: 700; font-size: 19px; fill: var(--logo-ink); }
  .tagline { font-family: "Montserrat", sans-serif; font-weight: 600; font-size: 17px; letter-spacing: 2px; fill: var(--white); }
  .product-name { font-family: "Oswald", sans-serif; font-weight: 700; fill: var(--white); }
  .net-weight { font-family: "Montserrat", sans-serif; font-weight: 700; font-size: 13px; fill: var(--white); }
</style>
</head>
<body>

<div class="bag bag--pumpkin">
  <svg viewBox="0 0 410 600">
    <defs>
      <linearGradient id="pumpkinBody" x1="0" y1="0" x2="1" y2="1">
        <stop offset="0" stop-color="var(--pumpkin-deep)"/>
        <stop offset="0.5" stop-color="var(--pumpkin-body)"/>
        <stop offset="1" stop-color="var(--pumpkin-deep)"/>
      </linearGradient>
      <linearGradient id="seedWindow" x1="0" y1="0" x2="1" y2="1">
        <stop offset="0" stop-color="#ece2c8"/>
        <stop offset="1" stop-color="#cbbd98"/>
      </linearGradient>
    </defs>
    <rect class="bag-base" width="410" height="600" fill="var(--white)"/>
    <path class="top-band" d="M0 0 H410 V4 L0 68 Z" fill="var(--pumpkin-top)"/>
    <path class="product-window" role="img" aria-label="Clear window showing shelled pumpkin seeds" d="M238 172 Q310 130 410 108 V312 Q330 250 238 172 Z" fill="url(#seedWindow)"/>
    <path class="body-panel" d="M0 232 L226 178 Q320 250 404 318 L410 322 V600 H0 Z" fill="url(#pumpkinBody)"/>
    <g class="brand">
      <circle cx="62" cy="148" r="14" fill="var(--logo-ink)"/>
      <text class="brand-name" x="84" y="155">Willowmere Acres</text>
    </g>
    <g transform="rotate(-14 40 300)">
      <text class="tagline" x="40" y="300">PREMIUM ORGANIC</text>
      <text class="product-name" x="36" y="414" font-size="112" textLength="330" lengthAdjust="spacingAndGlyphs">PUMPKIN</text>
      <text class="product-name" x="70" y="512" font-size="112" textLength="235" lengthAdjust="spacingAndGlyphs">SEEDS</text>
    </g>
    <text class="net-weight" x="30" y="566">200G</text>
    <g class="badges">
      <circle cx="268" cy="562" r="15" fill="var(--badge)"/>
      <circle cx="306" cy="562" r="15" fill="var(--badge)"/>
      <circle cx="344" cy="562" r="15" fill="var(--badge)"/>
    </g>
  </svg>
</div>

<div class="bag bag--nuts">
  <svg viewBox="0 0 410 600">
    <defs>
      <linearGradient id="nutsBody" x1="0" y1="0" x2="1" y2="1">
        <stop offset="0" stop-color="var(--nuts-deep)"/>
        <stop offset="0.5" stop-color="var(--nuts-body)"/>
        <stop offset="1" stop-color="var(--nuts-deep)"/>
      </linearGradient>
      <linearGradient id="nutsWindow" x1="0" y1="0" x2="1" y2="1">
        <stop offset="0" stop-color="#8a5535"/>
        <stop offset="0.5" stop-color="#b57f52"/>
        <stop offset="1" stop-color="#e0cba6"/>
      </linearGradient>
    </defs>
    <rect class="bag-base" width="410" height="600" fill="var(--white)"/>
    <path class="top-band" d="M0 0 H410 V4 L0 68 Z" fill="var(--nuts-top)"/>
    <path class="product-window" role="img" aria-label="Clear window showing mixed cashews, hazelnuts and almonds" d="M238 172 Q310 130 410 100 V312 Q330 250 238 172 Z" fill="url(#nutsWindow)"/>
    <path class="body-panel" d="M0 232 L226 178 Q320 250 404 318 L410 322 V600 H0 Z" fill="url(#nutsBody)"/>
    <g class="brand">
      <circle cx="62" cy="148" r="14" fill="var(--logo-ink)"/>
      <text class="brand-name" x="84" y="155">Willowmere Acres</text>
    </g>
    <g transform="rotate(-14 40 300)">
      <text class="tagline" x="40" y="300">PREMIUM ORGANIC</text>
      <text class="product-name" x="34" y="436" font-size="138" textLength="280" lengthAdjust="spacingAndGlyphs">DRIED</text>
      <text class="product-name" x="72" y="552" font-size="138" textLength="262" lengthAdjust="spacingAndGlyphs">NUTS</text>
    </g>
    <text class="net-weight" x="30" y="566">200G</text>
    <g class="badges">
      <circle cx="268" cy="562" r="15" fill="var(--badge)"/>
      <circle cx="306" cy="562" r="15" fill="var(--badge)"/>
      <circle cx="344" cy="562" r="15" fill="var(--badge)"/>
    </g>
  </svg>
</div>

</body>
</html>
```